Menu Board For a Bubble Tea Trailer

Berrisip is a bubble tea trailer that will be located in town and by the beach. Our aim is to bring refreshing beverages to our local community. My menu needs to reflect a bubbly and happy atmosphere of delicious fruit and some floral drinks, without looking unprofessional or childish.

My menu needs to be 1600mm long by 500mm high. It will be printed and attached to a sneeze guard for my beverage trailer which will be displayed on my serving window.

All drinks are priced as follows:
Regular: $6.50 Large: $7.50
Extra Topping: $0.60

Target Market(s)

Ages 15-39 including high school students, and young to middle aged workers that feel they need an energy or mood boost.

Industry/Entity Type

Bubble Tea (Non Alcoholic beverage)

Font styles to use
Sans Serif
Script

Colors
0094D4
00A9DD
6FCCEA
C7EBF8
E9F6FB
00AB8E
00BBA5
67D7C9
C6EFE9
E9F9F6
EE7325
F08F49
F5BC92
FAE3D3
FDF4ED
EB3D1F
EC4F4E
F09395
F8D3D4
FCEDEE

Requirements
Must have
• Pictures of bubble tea, Not crowded, easy to read, complimentary colours, prices, pictures must be in round bottom cups and without lid (attached)
Nice to have
• Bubbles or wave pattern
Should not have
• No black background, no fruits, no cartoon looking pictures

```html
<!DOCTYPE html>
<html lang="en">
<head>
<meta charset="utf-8">
<title>Bubble Tea Menu</title>
<link rel="stylesheet" href="https://fonts.googleapis.com/css2?family=Kaushan+Script&family=Lilita+One&family=Poppins:wght@400;600&family=Kalam:wght@400&display=swap">
<style>
  :root {
    --stage: #e9e9e9;
    --cream: #f6f2e8;
    --ink: #1c1c1c;
    --teal: #8fd0c9;
    --teal-deep: #25b5a6;
    --teal-light: #67d7c9;
    --coral: #e8706f;
    --peach-panel: #f4c1a9;
    --mint-panel: #c8e2c0;
    --price-chip: #8fd0c9;
    --orange: #f08f49;
    --amber: #e9a13a;
  }
  * { margin: 0; padding: 0; box-sizing: border-box; }
  html, body { width: 1200px; height: 571px; overflow: hidden; background: var(--stage); }
  body { position: relative; font-family: "Poppins", sans-serif; color: var(--ink); }

  .menu-board {
    position: absolute; left: 55px; top: 114px; width: 1100px; height: 344px;
    background: var(--cream); overflow: hidden;
  }
  .abs { position: absolute; }

  .art-area { border-radius: 0; }
  .art-wave { background: linear-gradient(160deg, var(--teal-light) 0%, rgba(103,215,201,0.35) 70%, rgba(246,242,232,0) 100%); }
  .art-splash-top { background: linear-gradient(180deg, rgba(233,161,58,0.85) 0%, rgba(240,143,73,0.55) 60%, rgba(246,242,232,0) 100%); }
  .art-splash-side { background: linear-gradient(90deg, rgba(233,161,58,0.75) 0%, rgba(240,143,73,0.35) 70%, rgba(246,242,232,0) 100%); }
  .art-corner { background: linear-gradient(135deg, rgba(103,215,201,0) 0%, var(--teal-light) 100%); }

  .title-band { left: 377px; top: 34px; width: 356px; height: 38px; background: var(--teal); border-radius: 4px; }
  .title {
    left: 0; width: 1100px; top: 6px; text-align: center;
    font-family: "Kaushan Script", cursive; font-size: 52px; line-height: 66px; font-weight: 400; color: var(--ink);
  }
  .bubble { border-radius: 50%; background: #3a2a1c; }

  .section-title {
    font-family: "Lilita One", sans-serif; font-size: 19px; line-height: 20px; font-weight: 400;
    letter-spacing: 0.5px; text-transform: uppercase; text-align: center; white-space: nowrap;
  }
  .section-title .green { color: var(--teal-deep); }
  .section-title .red { color: var(--coral); }
  .toppings-label { font-family: "Poppins", sans-serif; font-weight: 600; font-size: 20px; line-height: 24px; color: var(--coral); text-align: center; }
  .dash { stroke-width: 2; stroke-linecap: round; fill: none; }

  .panel { border-radius: 16px; }
  .panel-milk { left: 62px; top: 123px; width: 235px; height: 205px; background: var(--peach-panel); }
  .panel-tea { left: 412px; top: 123px; width: 235px; height: 139px; background: var(--teal); }
  .panel-toppings { left: 765px; top: 123px; width: 290px; height: 205px; background: var(--mint-panel); }

  .item { font-size: 14px; line-height: 16px; white-space: nowrap; }
  .item.wrap { white-space: normal; width: 80px; line-height: 16px; }
  .list-head { font-weight: 600; font-size: 17.5px; line-height: 20px; white-space: nowrap; }

  .cup-art { border-radius: 6px 6px 18px 18px; }
  .fruit-art { border-radius: 8px; }

  .price-intro { font-family: "Lilita One", sans-serif; font-size: 19.5px; line-height: 22px; color: #333; letter-spacing: 0.6px; }
  .price-label { font-family: "Kalam", cursive; font-size: 15px; line-height: 22px; color: var(--coral); white-space: nowrap; }
  .price-chip {
    display: inline-block; background: var(--price-chip); padding: 0 3px; margin-left: 2px;
    font-family: "Poppins", sans-serif; font-weight: 600; font-size: 16px; color: var(--ink); line-height: 20px;
  }
  .price-chip sup { font-size: 9px; vertical-align: 7px; }
</style>
</head>
<body>
<main class="menu-board">

  <div class="abs art-area art-wave" style="left:0; top:0; width:250px; height:74px;" role="img" aria-label="Teal and coral decorative wave"></div>
  <div class="abs art-area art-splash-top" style="left:829px; top:0; width:271px; height:60px;" role="img" aria-label="Splash of amber milk tea with flying pearls"></div>
  <div class="abs art-area art-splash-side" style="left:0; top:226px; width:50px; height:118px;" role="img" aria-label="Swirl of pouring milk tea"></div>
  <div class="abs art-area art-corner" style="left:1064px; top:306px; width:36px; height:38px;" role="img" aria-label="Teal decorative wave corner"></div>

  <div class="abs title-band"></div>
  <h1 class="abs title">Bubble Tea Menu</h1>
  <span class="abs bubble" style="left:328px;top:50px;width:14px;height:14px"></span>
  <span class="abs bubble" style="left:344px;top:57px;width:9px;height:9px"></span>
  <span class="abs bubble" style="left:355px;top:52px;width:7px;height:7px"></span>
  <span class="abs bubble" style="left:756px;top:50px;width:14px;height:14px"></span>
  <span class="abs bubble" style="left:772px;top:57px;width:9px;height:9px"></span>
  <span class="abs bubble" style="left:783px;top:52px;width:7px;height:7px"></span>

  <!-- Milk tea -->
  <h2 class="abs section-title" style="left:118px; top:95px; width:120px;">Milk Tea</h2>
  <svg class="abs" style="left:104px;top:97px" width="152" height="16" aria-hidden="true">
    <path class="dash" stroke="var(--coral)" d="M2 6 L12 3 M4 12 L13 10"/>
    <path class="dash" stroke="var(--teal-deep)" d="M140 3 L150 6 M139 10 L148 12"/>
  </svg>
  <section class="abs panel panel-milk" aria-label="Milk tea flavours"></section>
  <p class="abs item" style="left:90px;top:136px">Thai</p>
  <p class="abs item" style="left:90px;top:161px">Royal</p>
  <p class="abs item" style="left:90px;top:186px">original</p>
  <p class="abs item" style="left:90px;top:211px">Tiger Pearl</p>
  <p class="abs item wrap" style="left:90px;top:236px">Young Coconut</p>
  <p class="abs item" style="left:90px;top:277px">Watermelon</p>
  <p class="abs item" style="left:90px;top:302px">Banana</p>
  <p class="abs item" style="left:204px;top:136px">Taro</p>
  <p class="abs item" style="left:204px;top:161px">Lychee</p>
  <p class="abs item" style="left:204px;top:186px">Honeydew</p>
  <p class="abs item" style="left:204px;top:211px">Strawberry</p>
  <p class="abs item" style="left:204px;top:236px">Lavender</p>
  <p class="abs item" style="left:204px;top:261px">Mango</p>
  <p class="abs item" style="left:204px;top:286px">Rose</p>
  <div class="abs fruit-art" style="left:246px;top:290px;width:52px;height:32px;background:linear-gradient(90deg,#e0454a,#e8706f,#b73a3a)" role="img" aria-label="Strawberry, watermelon slice and rose"></div>

  <!-- Green / red tea -->
  <h2 class="abs section-title" style="left:419px; top:95px; width:220px;"><span class="green">Green Tea</span> / <span class="red">Red Tea</span></h2>
  <svg class="abs" style="left:403px;top:97px" width="252" height="16" aria-hidden="true">
    <path class="dash" stroke="var(--coral)" d="M2 6 L12 3 M4 12 L13 10"/>
    <path class="dash" stroke="var(--teal-deep)" d="M240 3 L250 6 M239 10 L248 12"/>
  </svg>
  <section class="abs panel panel-tea" aria-label="Green and red tea flavours"></section>
  <p class="abs item" style="left:435px;top:136px">Peach</p>
  <p class="abs item" style="left:435px;top:161px">Mango</p>
  <p class="abs item" style="left:435px;top:186px">Passionfruit</p>
  <p class="abs item" style="left:435px;top:211px">Watermelon</p>
  <p class="abs item" style="left:435px;top:236px">Dragonfruit</p>
  <p class="abs item" style="left:537px;top:136px">Grape</p>
  <p class="abs item" style="left:537px;top:161px">Lychee</p>
  <p class="abs item" style="left:537px;top:186px">Strawberry</p>
  <p class="abs item" style="left:537px;top:211px">Green Apple</p>
  <p class="abs item" style="left:537px;top:236px">Pomegranate</p>
  <div class="abs cup-art" style="left:371px;top:174px;width:58px;height:76px;background:linear-gradient(180deg,#dfe8d8,#8dbb4a 40%,#5a6b2c)" role="img" aria-label="Green bubble tea in a round-bottom cup"></div>
  <div class="abs cup-art" style="left:625px;top:132px;width:52px;height:78px;background:linear-gradient(180deg,#dde8e4,#ec7a3a 40%,#8a3d1a)" role="img" aria-label="Red tea with pearls and a straw in a round-bottom cup"></div>

  <!-- Prices -->
  <p class="abs price-intro" style="left:346px;top:278px">ALL DRINKS ARE<br>PRICED AS.....</p>
  <p class="abs price-label" style="left:513px;top:273px">Regular : <span class="price-chip"><sup>$</sup>6.50</span>&nbsp;&nbsp;Large : <span class="price-chip"><sup>$</sup>7.50</span></p>
  <p class="abs price-label" style="left:513px;top:302px">Extra Topping <span class="price-chip"><sup>$</sup>0.60</span></p>

  <!-- Toppings -->
  <h2 class="abs section-title" style="left:822px; top:77px; width:170px;">Tapioca&nbsp; Pearls</h2>
  <p class="abs toppings-label" style="left:822px; top:95px; width:170px;">Toppings</p>
  <svg class="abs" style="left:800px;top:78px" width="214" height="16" aria-hidden="true">
    <path class="dash" stroke="var(--teal-deep)" d="M2 6 L12 3 M4 12 L13 10"/>
    <path class="dash" stroke="var(--coral)" d="M202 3 L212 6 M201 10 L210 12"/>
  </svg>
  <section class="abs panel panel-toppings" aria-label="Topping choices"></section>
  <h3 class="abs list-head" style="left:786px;top:137px">Fruit Jelly</h3>
  <h3 class="abs list-head" style="left:901px;top:137px">Popping Pearls</h3>
  <p class="abs item" style="left:788px;top:168px">Rainbow</p>
  <p class="abs item" style="left:788px;top:193px">Lychee</p>
  <p class="abs item" style="left:788px;top:218px">Mango</p>
  <p class="abs item" style="left:788px;top:243px">Peach</p>
  <p class="abs item" style="left:788px;top:268px">Grape</p>
  <p class="abs item" style="left:902px;top:166px">Peach</p>
  <p class="abs item" style="left:902px;top:191px">Mango</p>
  <p class="abs item" style="left:902px;top:216px">Lychee</p>
  <p class="abs item" style="left:902px;top:241px">Strawberry</p>
  <p class="abs item" style="left:902px;top:266px">Passionfruit</p>
  <p class="abs item" style="left:902px;top:291px">Watermelon</p>
  <div class="abs fruit-art" style="left:790px;top:292px;width:70px;height:32px;background:linear-gradient(90deg,#f5a05c,#e0454a,#d83a3a)" role="img" aria-label="Peach, watermelon slice and strawberry"></div>
  <div class="abs cup-art" style="left:1013px;top:210px;width:56px;height:116px;background:linear-gradient(180deg,#e3ece6,#e89248 30%,#a8591f 80%,#3a2a1c)" role="img" aria-label="Tall orange milk tea with pearls and a straw in a round-bottom cup"></div>

</main>
</body>
</html>
```